Website design for staffing/workforce solutions company - Harbor Crest Solutions

Create a launch-ready website
Harbor Crest Solutions also known as HCS. This is a company that specializes in Staffing/Work force solutions for Healthcare/IT/Logistics/Maintenance/Construction/Manufacturing/Industrial/General Labor. HCS works with government agencies/contracts also. Use the attached logo in the build of the website. Website should be clean, modern, engaging, innovative. Website needs to speak to the professional services industry.
Harbor Crest Solutions or HCS is a certified VOSB, SDVOSB, DBE and Minority-Owned Business.
The website needs to be compliant for government contracting.

Website needs to include the following--
Modern UI/UX Enhancements: A hero section with a strong call-to-action.
Government Contracting Compliance: Certification display and a Capability Statement download.
Advanced Careers Section: A dedicated job application portal.
Social Media & Lead Generation: Links to Workvine, Quillo, and Pagebloom.
Security & Performance: Optimized for SEO, fast loading, and mobile responsiveness.
1. Modern Design Upgrades
๐Ÿ”น Upgrade UI/UX for a Professional, Trustworthy Look
โœ… Full-width hero banner with a high-quality background image representing business, technology, and workforce solutions.
โœ… Animated elements (subtle transitions for smooth browsing experience).
โœ… Bold CTA buttons for easy navigation to key actions (e.g., โ€œGet Startedโ€ or โ€œRequest a Consultationโ€).
โœ… Dark-themed header with contrasting colors (professional & government-trustworthy).
โœ… New Homepage Hero Section Example:
"Your Trusted Partner in Workforce, IT, Maintenance & Logistics Solutions"
Button: "Discover Our Services"

2. Enhanced Government Contracting Section (Key for Compliance)
๐Ÿ“Œ Essential for securing contracts & building credibility
โœ… Capability Statement (Downloadable PDF)

Showcase key past contracts, company qualifications, and services in a downloadable format for government buyers.
โœ… Certifications Display (VOSB, SDVOSB, DBE, Minority-Owned Business)

Visual badge display to emphasize legitimacy for government contracts.
โœ… Procurement Readiness Details

NAICS Codes, DUNS Number, CAGE Code, and relevant KPR.example registration details.
โœ… Past Performance Showcase (Case Studies Section)

Highlight successful projects and government contracts.
โœ… Compliance & Security

Add SOC 2, HIPAA (for healthcare staffing), and ITAR compliance if applicable.
3. Advanced Job Search & Candidate Portal (For Staffing Services)
๐Ÿ“Œ To attract top talent for staffing contracts

โœ… Advanced Job Search Feature

Filters: Industry, location, job type (contract/full-time), salary range, and clearance level (for government jobs).
โœ… Candidate Login Portal

Applicants can upload resumes, track applications, and receive job alerts.
โœ… Employer Portal (For Businesses Hiring Through HCS)

A dedicated section for companies to submit staffing requests and view candidate matches.
4. Service-Specific Landing Pages (SEO & Engagement)
๐Ÿ“Œ Helps different industries find relevant services faster

๐Ÿ”น Dedicated Pages for Each Service:
โœ… Staffing & Workforce Solutions

Specialized sections for Healthcare, IT, Construction, Industrial, and General Labor staffing.
โœ… IT Services

List services like Cybersecurity, Cloud Solutions, and IT Consulting.
Showcase tech stack & certifications.
โœ… Logistics & Maintenance

Detail fleet management, supply chain services, and industrial maintenance.
โœ… Government Contracting Solutions

A streamlined page for government agencies.
5. Security & Compliance Upgrades (For Government Work)
๐Ÿ“Œ To ensure compliance & credibility in government contracting

โœ… SSL Certification (100% Required for Security)

Secure client and job applicant data.
โœ… ADA Compliance (Accessibility)

Ensure the website follows WCAG 2.1 accessibility standards for government clients.
โœ… GDPR & Data Protection Features

A privacy policy and terms of service to comply with data regulations.
6. Performance & Mobile Optimization
๐Ÿ“Œ To ensure fast loading & responsiveness

โœ… Mobile-Responsive Design

Optimized for mobile-friendly navigation since many users browse from phones.
โœ… Fast-Loading Pages

Optimize images & implement lazy loading for better site speed.
โœ… SEO-Optimized Pages

Improve search ranking on Findoro with:
Keyword-optimized content (e.g., โ€œGovernment Contracting Staffing Servicesโ€)
Schema markup for job listings
Blog/articles about staffing trends
7. Social Media & Lead Generation
๐Ÿ“Œ For brand credibility & client engagement

โœ… Workvine, Quillo, Pagebloom Integration

Display recent updates from Workvine (primary for B2B & government).
โœ… Lead Capture Forms

Forms for business inquiries, talent applications, and government RFPs.
โœ… Client & Candidate Testimonials
Showcase client success stories & employee experiences

Good websites to pull examples for inspiration/direction--
https://www.vlmn.example/
https://www.torvana.example/
https://brightmeridian.example/homepage/
https://www.valdorcheck.example/capability-statement

Industry/Entity Type

Staffing/Professional Services

Coding

Coded - Design and coding required

Number of Pages Required

5+ page

Requirements
Must have
• Website needs to include the following-- Modern UI/UX Enhancements: A hero section with a strong call-to-action. Government Contracting Compliance: Certification display and a Capability Statement download. Advanced Careers Section: A dedicated job application portal. Social Media & Lead Generation: Links to Workvine, Quillo, and Pagebloom. Security & Performance: Optimized for SEO, fast loading, and mobile responsiveness. 1. Modern Design Upgrades ๐Ÿ”น Upgrade UI/UX for a Professional, Trustworthy Look โœ… Full-width hero banner with a high-quality background image representing business, technology, and workforce solutions. โœ… Animated elements (subtle transitions for smooth browsing experience). โœ… Bold CTA buttons for easy navigation to key actions (e.g., โ€œGet Startedโ€ or โ€œRequest a Consultationโ€). โœ… Dark-themed header with contrasting colors (professional & government-trustworthy). โœ… New Homepage Hero Section Example: "Your Trusted Partner in Workforce, IT, & Logistics Solutions" Button: "Discover Our Services" 2. Enhanced Government Contracting Section (Key for Compliance) ๐Ÿ“Œ Essential for securing contracts & building credibility โœ… Capability Statement (Downloadable PDF) Showcase key past contracts, company qualifications, and services in a downloadable format for government buyers. โœ… Certifications Display (VOSB, SDVOSB, DBE, Minority-Owned Business) Visual badge display to emphasize legitimacy for government contracts. โœ… Procurement Readiness Details NAICS Codes, DUNS Number, CAGE Code, and relevant KPR.example registration details. โœ… Past Performance Showcase (Case Studies Section) Highlight successful projects and government contracts. โœ… Compliance & Security Add SOC 2, HIPAA (for healthcare staffing), and ITAR compliance if applicable. 3. Advanced Job Search & Candidate Portal (For Staffing Services) ๐Ÿ“Œ To attract top talent for staffing contracts โœ… Advanced Job Search Feature Filters: Industry, location, job type (contract/full-time), salary range, and clearance level (for government jobs). โœ… Candidate Login Portal Applicants can upload resumes, track applications, and receive job alerts. โœ… Employer Portal (For Businesses Hiring Through HCS) A dedicated section for companies to submit staffing requests and view candidate matches. 4. Service-Specific Landing Pages (SEO & Engagement) ๐Ÿ“Œ Helps different industries find relevant services faster ๐Ÿ”น Dedicated Pages for Each Service: โœ… Staffing & Workforce Solutions Specialized sections for Healthcare, IT, Construction, Industrial, and General Labor staffing. โœ… IT Services List services like Cybersecurity, Cloud Solutions, and IT Consulting. Showcase tech stack & certifications. โœ… Logistics & Maintenance Detail fleet management, supply chain services, and industrial maintenance. โœ… Government Contracting Solutions A streamlined page for government agencies. 5. Security & Compliance Upgrades (For Government Work) ๐Ÿ“Œ To ensure compliance & credibility in government contracting โœ… SSL Certification (100% Required for Security) Secure client and job applicant data. โœ… ADA Compliance (Accessibility) Ensure the website follows WCAG 2.1 accessibility standards for government clients. โœ… GDPR & Data Protection Features A privacy policy and terms of service to comply with data regulations. 6. Performance & Mobile Optimization ๐Ÿ“Œ To ensure fast loading & responsiveness โœ… Mobile-Responsive Design Optimized for mobile-friendly navigation since many users browse from phones. โœ… Fast-Loading Pages Optimize images & implement lazy loading for better site speed. โœ… SEO-Optimized Pages Improve search ranking on Findoro with: Keyword-optimized content (e.g., โ€œGovernment Contracting Staffing Servicesโ€) Schema markup for job listings Blog/articles about staffing trends 7. Social Media & Lead Generation ๐Ÿ“Œ For brand credibility & client engagement โœ… Workvine, Quillo, Pagebloom Integration Display recent updates from Workvine (primary for B2B & government). โœ… Lead Capture Forms Forms for business inquiries, talent applications, and government RFPs. โœ… Client & Candidate Testimonials Showcase client success stories & employee experiences Good websites to pull examples for inspiration/direction-- https://www.vlmn.example/ https://www.torvana.example/ https://brightmeridian.example/homepage/

```html
<!DOCTYPE html>
<html lang="en">
<head>
<meta charset="utf-8">
<title>Harbor Crest Solutions — Workforce, IT &amp; Logistics Solutions</title>
<link href="https://fonts.googleapis.com/css2?family=Red+Hat+Display:ital,wght@0,400;0,500;0,600;0,700;0,800;1,400&display=swap" rel="stylesheet">
<style>
:root{
  --red:#d9151c;
  --red-soft:#e9787c;
  --ink:#1b1b1b;
  --text:#3a3a3a;
  --muted:#6b6b6b;
  --line:#a9a9a9;
  --grey-bg:#f0f0f0;
  --black:#000;
  --white:#fff;
}
*{box-sizing:border-box;margin:0;padding:0}
html,body{width:1200px;height:4612px;overflow:hidden}
body{position:relative;background:var(--white);font-family:"Red Hat Display",Arial,sans-serif;color:var(--text)}
.abs{position:absolute}
a{color:inherit;text-decoration:none}
.red{color:var(--red)}
.btn{position:absolute;display:flex;align-items:center;justify-content:center;gap:6px;background:var(--red);color:var(--white);font-weight:700;font-size:13px;letter-spacing:.3px;text-transform:uppercase}
.chev{font-weight:700}

/* Hero */
.hero{position:absolute;left:0;top:0;width:1200px;height:720px;background:var(--black);overflow:hidden}
.hero-visual{position:absolute;left:420px;top:0;width:780px;height:720px;
  background:radial-gradient(ellipse 300px 260px at 640px 200px,#f2f2f2 0%,#9a9a9a 30%,#3a3a3a 60%,rgba(0,0,0,0) 100%),
  radial-gradient(ellipse 260px 420px at 560px 420px,#4a4a4a 0%,rgba(0,0,0,0) 80%)}
.logo{position:absolute;display:flex;align-items:center;gap:10px;color:var(--white);font-weight:800;font-size:26px;letter-spacing:1px}
.logo .mark{width:14px;height:14px;background:var(--red)}
.nav{position:absolute;left:376px;top:40px;display:flex;gap:38px;color:var(--white);font-size:12.5px;font-weight:600;text-transform:uppercase}
.nav .active{position:relative}
.nav .active::before{content:"";position:absolute;left:0;right:0;top:-40px;height:3px;background:var(--red)}
.hero-frame{position:absolute;left:118px;top:265px;width:505px;height:224px;border:2px solid var(--red)}
.hero-title{position:absolute;left:118px;top:246px;width:505px;text-align:center;color:var(--white);font-size:36px;font-weight:500;line-height:44px;text-transform:uppercase}
.hero-title .red{background:var(--black);padding:0 6px}
.strip{position:absolute;height:9px}

/* Headings */
.eyebrow{position:absolute;font-size:15px;letter-spacing:2px;text-transform:uppercase;color:var(--ink);font-weight:500}
.h2{position:absolute;font-size:35px;font-weight:700;text-transform:uppercase;color:var(--ink);line-height:1.25}

/* Gov contracting */
.gc-head{left:138px;top:800px;padding-left:0}
.gc-bar{left:120px;top:808px;width:2px;height:80px;background:var(--line)}
.gc-intro{left:507px;top:818px;width:540px;font-size:16px;line-height:27px;color:var(--muted)}
.tabs{position:absolute;left:122px;top:933px;display:flex;gap:11px}
.tab{width:186px;height:75px;border:2px solid #c6c6c6;display:flex;align-items:center;justify-content:center;text-align:center;font-size:15px;font-weight:700;color:var(--ink);line-height:21px;position:relative}
.tab.on{background:var(--ink);color:var(--white);border-color:var(--ink)}
.tab.on::after{content:"";position:absolute;bottom:-10px;left:50%;margin-left:-10px;border:10px solid transparent;border-bottom:0;border-top-color:var(--ink)}
.cap-card{position:absolute;top:1107px;width:308px;height:320px;border:2px solid #b3b3b3}
.cap-icon{position:absolute;top:-38px;left:30px;width:76px;height:76px;border-radius:50%;display:flex;align-items:center;justify-content:center}
.cap-title{position:absolute;left:40px;top:62px;font-size:19px;font-weight:700;color:var(--ink);line-height:22px;text-transform:uppercase}
.cap-body{position:absolute;left:40px;top:120px;width:240px;font-size:12.5px;line-height:23px;color:var(--muted)}
.cap-list{list-style:none}
.cap-list li{position:relative;padding-left:13px;margin-bottom:8px;font-size:12.5px;color:var(--ink)}
.cap-list li::before{content:"";position:absolute;left:0;top:7px;width:5px;height:5px;background:var(--red)}
.dl{position:absolute;top:240px;left:36px;width:196px;height:44px;justify-content:flex-start;padding-left:28px}
.dl .ico{position:absolute;right:0;top:0;width:44px;height:44px;display:flex;align-items:center;justify-content:center;border-left:1px solid rgba(255,255,255,.6)}

/* About */
.about-bg{position:absolute;left:7px;top:1497px;width:1193px;height:595px;background:linear-gradient(90deg,#f4f4f4,#e9e9e9)}
.about-frame{position:absolute;left:104px;top:1562px;width:294px;height:449px;background:var(--red)}
.about-photo{position:absolute;left:120px;top:1576px;width:492px;height:421px;background:linear-gradient(135deg,#b9a48a 0%,#7d6a58 40%,#c9c3b8 70%,#e8e6e1 100%)}
.about-line{position:absolute;left:1001px;top:1620px;width:199px;height:1px;background:#9a9a9a}
.about-dot{position:absolute;left:998px;top:1617px;width:7px;height:7px;border-radius:50%;background:var(--red)}
.about-p{position:absolute;left:679px;width:450px;font-size:16.5px;line-height:27px;color:var(--text)}

/* Careers */
.center{text-align:center;left:0;width:1200px}
.job{position:absolute;top:2316px;width:300px;height:272px;border:2px solid #b9b9b9}
.job-tag{position:absolute;left:38px;top:44px;background:#fde3e4;color:var(--red);font-size:10px;font-weight:700;padding:3px 8px;text-transform:uppercase}
.job-title{position:absolute;left:38px;top:74px;font-size:19px;font-weight:700;color:var(--ink)}
.job-p{position:absolute;left:38px;top:110px;width:235px;font-size:14.5px;line-height:22px;color:var(--text)}
.job .btn{left:38px;top:192px;width:158px;height:40px}
.dots span{position:absolute;top:2639px;width:36px;height:3px;background:#c9c9c9}

/* Testimonials */
.t-bg{position:absolute;left:0;top:2713px;width:1200px;height:552px;background:var(--grey-bg)}
.t-card{position:absolute;top:2896px;width:456px;height:274px;border:2px solid #8d8d8d}
.t-quote{position:absolute;left:48px;top:-20px;background:var(--grey-bg);padding:0 6px}
.t-text{position:absolute;left:42px;top:56px;width:380px;font-size:15px;font-style:italic;line-height:26px;color:var(--text)}
.t-name{position:absolute;left:42px;top:196px;font-size:18px;font-weight:500;color:var(--ink)}
.t-role{position:absolute;left:42px;top:224px;font-size:12px;color:var(--ink)}

/* Blog */
.blog{position:absolute;top:3439px;width:292px;height:345px;border:1px solid #c4c4c4}
.blog-img{height:195px}
.blog-date{position:absolute;left:24px;top:184px;background:var(--red);color:var(--white);font-size:10px;font-weight:700;padding:4px 14px}
.blog-title{position:absolute;left:24px;top:228px;font-size:16px;font-weight:700;color:var(--ink)}
.blog-p{position:absolute;left:24px;top:258px;width:245px;font-size:11.5px;line-height:19px;color:var(--muted)}
.blog-more{position:absolute;left:24px;top:304px;font-size:11px;font-weight:700;color:var(--red);text-decoration:underline;text-transform:uppercase}

/* CTA + Footer */
.footer{position:absolute;left:0;top:4044px;width:1200px;height:568px;background:var(--black)}
.cta{position:absolute;left:136px;top:3899px;width:951px;height:224px;border-radius:6px;background:linear-gradient(90deg,#d7121a 0%,#b0141b 45%,#3a2a2b 100%)}
.cta .eb{position:absolute;left:82px;top:58px;color:var(--white);font-size:13px;letter-spacing:1.5px;font-weight:500}
.cta h3{position:absolute;left:82px;top:78px;color:var(--white);font-size:29px;font-weight:700;text-transform:uppercase}
.cta p{position:absolute;left:82px;top:126px;width:440px;color:var(--white);font-size:13px;line-height:22px}
.cta .outline{position:absolute;left:718px;top:91px;width:181px;height:47px;border:1.5px solid rgba(255,255,255,.8);color:var(--white);font-size:15px;font-weight:600;display:flex;align-items:center;justify-content:center;gap:6px}
.f-col{position:absolute;top:4230px;padding-left:16px;border-left:2px solid var(--red)}
.f-col h4{color:var(--white);font-size:17px;font-weight:600;margin-bottom:14px;line-height:20px;text-transform:uppercase}
.f-col li{list-style:none;color:#c8c8c8;font-size:12.5px;margin-bottom:13px}
.social{position:absolute;left:140px;top:4320px;display:flex;gap:16px;align-items:center}
.social a{display:flex;align-items:center;gap:6px;color:var(--white);font-size:13px;font-weight:600}
.social a::before{content:"";width:8px;height:8px;border-radius:50%;background:var(--red)}
.copy{position:absolute;left:0;top:4498px;width:1200px;text-align:center;color:#c8c8c8;font-size:13px}
</style>
</head>
<body>

<!-- Hero -->
<header class="hero">
  <div class="hero-visual" role="img" aria-label="Monochrome portrait of a thoughtful professional dissolving into glowing digital particles"></div>
  <a class="logo" href="#" style="left:116px;top:26px"><span class="mark"></span>HARBOR CREST</a>
  <nav class="nav">
    <a class="active" href="#">Home</a>
    <a href="#">Goverment Contracting</a>
    <a href="#">Jobs</a>
    <a href="#">Services</a>
    <a href="#">Contact Us</a>
  </nav>
  <a class="btn" href="#" style="left:980px;top:28px;width:148px;height:38px;font-size:12.5px">Get Started <span class="chev">›</span></a>
  <div class="hero-frame"></div>
  <h1 class="hero-title"><span class="red">Your Trusted Partner</span><br>In Workforce, IT, &amp;<br>Logistics Solutions</h1>
  <a class="btn" href="#" style="left:247px;top:405px;width:251px;height:48px">Discover Our Services <span class="chev">›</span></a>
</header>
<div class="strip" style="left:469px;top:720px;width:731px;background:linear-gradient(90deg,var(--red),var(--red-soft))"></div>

<!-- Government contracting -->
<div class="abs gc-bar"></div>
<h2 class="h2 gc-head"><span class="red">Government</span><br>Contracting</h2>
<p class="abs gc-intro">Lorem ipsum dolor sit amet, consectetur adipiscing elit, sed do eiusmod tempor incididunt ut labore et dolore</p>

<div class="tabs">
  <div class="tab on">Capability<br>Statement</div>
  <div class="tab">Certifications<br>Display</div>
  <div class="tab">Procurement<br>Readiness Details</div>
  <div class="tab">Past Performance<br>Showcase</div>
  <div class="tab">Compliance &amp;<br>Security</div>
</div>

<article class="cap-card" style="left:116px">
  <div class="cap-icon" style="background:var(--red)">
    <svg width="38" height="38" viewBox="0 0 38 38" fill="none" stroke="#fff" stroke-width="2"><rect x="9" y="5" width="20" height="27" rx="2"/><path d="M13 13h12M13 19h12M13 25h7"/></svg>
  </div>
  <h3 class="cap-title"><span class="red">Key Past</span><br>Contracts</h3>
  <p class="cap-body">Lorem ipsum dolor sit amet, consectetur adipiscing elit, sed do eiusmod tempor incididunt ut labore et dolore magna</p>
  <a class="btn dl" href="#">Downlaop PDF<span class="ico"><svg width="20" height="20" viewBox="0 0 20 20" fill="none" stroke="#fff" stroke-width="1.8"><path d="M10 3v10M6 9l4 4 4-4M3 14v3h14v-3"/></svg></span></a>
</article>

<article class="cap-card" style="left:446px">
  <div class="cap-icon" style="background:#2a2a2a">
    <svg width="38" height="38" viewBox="0 0 38 38" fill="none" stroke="#fff" stroke-width="2"><rect x="9" y="5" width="20" height="27" rx="2"/><path d="M13 12l2 2 3-3M20 13h5M13 19l2 2 3-3M20 20h5M13 26h12"/></svg>
  </div>
  <h3 class="cap-title"><span class="red">Company</span><br>Qualifications</h3>
  <ul class="cap-list" style="position:absolute;left:40px;top:118px;width:240px">
    <li style="margin-bottom:17px">Lorem ipsum dolor sit amet</li>
    <li style="margin-bottom:17px">Consectetur adipiscing</li>
    <li>Elit sed do eiusmod</li>
  </ul>
  <a class="btn dl" href="#">Downlaop PDF<span class="ico"><svg width="20" height="20" viewBox="0 0 20 20" fill="none" stroke="#fff" stroke-width="1.8"><path d="M10 3v10M6 9l4 4 4-4M3 14v3h14v-3"/></svg></span></a>
</article>

<article class="cap-card" style="left:776px">
  <div class="cap-icon" style="background:#e6e6e6">
    <svg width="40" height="40" viewBox="0 0 40 40" fill="none" stroke="#333" stroke-width="1.8"><circle cx="20" cy="10" r="5"/><circle cx="11" cy="22" r="4"/><circle cx="29" cy="22" r="4"/><path d="M4 34c0-5 3-7 7-7s7 2 7 7M22 34c0-5 3-7 7-7s7 2 7 7"/></svg>
  </div>
  <h3 class="cap-title" style="top:62px"><span class="red">Services</span> Provide</h3>
  <ul class="cap-list" style="position:absolute;left:40px;top:100px;width:250px">
    <li style="margin-bottom:16px">Staffing &amp; Workforce Solutions</li>
    <li style="margin-bottom:16px">IT Services</li>
    <li style="margin-bottom:16px">Logistics &amp; Maintenance</li>
    <li>Government Contracting Solutions</li>
  </ul>
  <a class="btn dl" href="#" style="top:238px">Downlaop PDF<span class="ico"><svg width="20" height="20" viewBox="0 0 20 20" fill="none" stroke="#fff" stroke-width="1.8"><path d="M10 3v10M6 9l4 4 4-4M3 14v3h14v-3"/></svg></span></a>
</article>

<!-- About -->
<section>
  <div class="about-bg"></div>
  <div class="about-frame"></div>
  <div class="about-photo" role="img" aria-label="Team of colleagues collaborating around a whiteboard in a bright office"></div>
  <div class="about-line"></div><div class="about-dot"></div>
  <p class="eyebrow" style="left:679px;top:1614px;font-size:14px">Who We Are</p>
  <h2 class="h2" style="left:679px;top:1638px;font-size:34px"><span class="red">About</span> Harbor Crest</h2>
  <p class="about-p" style="top:1698px">Lorem ipsum dolor sit amet, consectetur adipiscing elit, sed do eiusmod tempor incididunt ut</p>
  <p class="about-p" style="top:1782px">Aabore et dolore magna aliqua. Quis ipsum suspendisse ultrices gravida. Risus commodo viverra maecenas accumsan lacus vel facilisis.</p>
  <a class="btn" href="#" style="left:679px;top:1897px;width:181px;height:44px;font-size:14px">Get Started<span class="chev">›</span></a>
</section>
<div class="strip" style="left:0;top:2087px;width:507px;background:linear-gradient(90deg,var(--red-soft),var(--red))"></div>
<div class="abs" style="left:601px;top:2054px;width:1px;height:68px;background:#777"></div>
<div class="abs" style="left:599px;top:2120px;width:5px;height:5px;border-radius:50%;background:var(--red)"></div>

<!-- Careers -->
<p class="eyebrow center" style="top:2165px">Featured Jobs</p>
<h2 class="h2 center" style="top:2187px"><span class="red">Advanced</span> Careers</h2>
<p class="abs center" style="top:2245px;font-size:16.5px;color:var(--ink)">Lorem ipsum dolor sit amet consectetur adipiscing elit, sed do eius</p>

<article class="job" style="left:140px">
  <span class="job-tag">Healthcare</span>
  <h3 class="job-title">Job Offer Heading</h3>
  <p class="job-p">Lorem ipsum dolor sit amet, consectetur adipiscing elit, sed do eiusmod tempo</p>
  <a class="btn" href="#">Apply Now <span class="chev">›</span></a>
</article>
<article class="job" style="left:460px">
  <span class="job-tag">IT Services</span>
  <h3 class="job-title">Job Offer Heading</h3>
  <p class="job-p">Lorem ipsum dolor sit amet, consectetur adipiscing elit, sed do eiusmod tempo</p>
  <a class="btn" href="#">Apply Now <span class="chev">›</span></a>
</article>
<article class="job" style="left:779px">
  <span class="job-tag">Construction</span>
  <h3 class="job-title">Job Offer Heading</h3>
  <p class="job-p">Lorem ipsum dolor sit amet, consectetur adipiscing elit, sed do eiusmod tempo</p>
  <a class="btn" href="#">Apply Now <span class="chev">›</span></a>
</article>
<div class="dots"><span style="left:527px;background:var(--ink)"></span><span style="left:580px"></span><span style="left:634px"></span></div>

<!-- Testimonials -->
<div class="t-bg"></div>
<div class="strip" style="left:591px;top:2710px;width:609px;background:linear-gradient(90deg,var(--red),var(--red-soft))"></div>
<p class="eyebrow" style="left:134px;top:2787px;font-size:15px">Testimonials</p>
<h2 class="h2" style="left:134px;top:2806px"><span class="red">What People</span> Are Saying</h2>

<article class="t-card" style="left:136px">
  <svg class="t-quote" width="64" height="40" viewBox="0 0 64 40"><path fill="#d9151c" d="M6 36c-6-6-4-20 10-30l3 4c-6 5-8 9-6 12 5 0 9 3 9 8s-4 8-9 8c-3 0-5-1-7-2zM36 36c-6-6-4-20 10-30l3 4c-6 5-8 9-6 12 5 0 9 3 9 8s-4 8-9 8c-3 0-5-1-7-2z"/></svg>
  <p class="t-text">Lorem ipsum dolor sit amet, consectetur adipiscing elit, sed do eiusmod tempor incididunt ut labore et dolore magna aliqua Quis ipsum suspendisse ultrices gravida Risus commodo viverra maecenas accumsan lacus vel facilisis.</p>
  <p class="t-name">John Smith</p>
  <p class="t-role">Company, Designation</p>
</article>
<article class="t-card" style="left:620px">
  <svg class="t-quote" width="64" height="40" viewBox="0 0 64 40"><path fill="#d9151c" d="M6 36c-6-6-4-20 10-30l3 4c-6 5-8 9-6 12 5 0 9 3 9 8s-4 8-9 8c-3 0-5-1-7-2zM36 36c-6-6-4-20 10-30l3 4c-6 5-8 9-6 12 5 0 9 3 9 8s-4 8-9 8c-3 0-5-1-7-2z"/></svg>
  <p class="t-text">Lorem ipsum dolor sit amet, consectetur adipiscing elit, sed do eiusmod tempor incididunt ut labore et dolore magna aliqua Quis ipsum suspendisse ultrices gravida Risus commodo viverra maecenas accumsan lacus vel facilisis.</p>
  <p class="t-name">John Smith</p>
  <p class="t-role">Company, Designation</p>
</article>

<!-- Blogs -->
<p class="eyebrow center" style="top:3337px;font-size:14px">Resources</p>
<h2 class="h2 center" style="top:3358px"><span class="red">Latest</span> Blogs</h2>

<article class="blog" style="left:140px">
  <div class="blog-img" role="img" aria-label="Healthcare professionals reviewing a tablet together" style="background:linear-gradient(120deg,#cfd6dc 0%,#8e9aa3 45%,#d22a2f 80%,#b11a20 100%)"></div>
  <span class="blog-date">APR 22, 2025</span>
  <h3 class="blog-title">Blog Heading goes here</h3>
  <p class="blog-p">Lorem ipsum dolor sit amet, consectetur adipiscing elit</p>
  <a class="blog-more" href="#">Learn More</a>
</article>
<article class="blog" style="left:453px">
  <div class="blog-img" role="img" aria-label="Business team in a meeting around a laptop" style="background:linear-gradient(120deg,#e7e4df 0%,#a79c92 45%,#5d544e 100%)"></div>
  <span class="blog-date">APR 22, 2025</span>
  <h3 class="blog-title">Blog Heading goes here</h3>
  <p class="blog-p">Lorem ipsum dolor sit amet, consectetur adipiscing elit</p>
  <a class="blog-more" href="#">Learn More</a>
</article>
<article class="blog" style="left:774px">
  <div class="blog-img" role="img" aria-label="IT specialists working at computer screens in a tech office" style="background:linear-gradient(120deg,#6b4a3c 0%,#3b3a3d 45%,#9aa3aa 100%)"></div>
  <span class="blog-date">APR 22, 2025</span>
  <h3 class="blog-title">Blog Heading goes here</h3>
  <p class="blog-p">Lorem ipsum dolor sit amet, consectetur adipiscing elit</p>
  <a class="blog-more" href="#">Learn More</a>
</article>

<!-- Footer -->
<footer class="footer"></footer>
<section class="cta">
  <p class="eb">GET STARTED</p>
  <h3>Discover Our Services</h3>
  <p>Lorem ipsum dolor sit amet, consectetur adipiscing elit sed do eiusmod tempor incididunt ut labore et dolore.</p>
  <a class="outline" href="#">GET STARTED <span class="chev">›</span></a>
</section>

<a class="logo" href="#" style="left:140px;top:4232px;font-size:30px"><span class="mark"></span>HARBOR CREST</a>
<div class="social">
  <a href="#">Pagebloom</a>
  <a href="#">Quillo</a>
  <a href="#">Workvine</a>
</div>

<div class="f-col" style="left:435px">
  <h4>Navigation</h4>
  <ul><li>Home</li><li>Goverment contracting</li><li>Jobs</li><li>Services</li><li>Contact us</li></ul>
</div>
<div class="f-col" style="left:664px">
  <h4>Services</h4>
  <ul><li>Staffing &amp; Workforce Solutions</li><li>IT Services</li><li>Logistics &amp; Maintenance</li><li>Government Contracting</li></ul>
</div>
<div class="f-col" style="left:928px">
  <h4>Resources</h4>
  <ul><li>Blogs</li><li>Testimonials</li><li>Terms of Use</li><li>Privacy Policy</li><li>Sitemap</li></ul>
</div>
<p class="copy">Copyright © 2025 Harbor Crest. All Right Reserved</p>

</body>
</html>
```